Tri-Fold Menu of Services for our Eyelash and Skin Care Spa

We need a beautiful spa service menu for our upscale spa in St. Charles Missouri. We specialize in providing treatments that are specific to the clients needs. Our services are eyelash extensions, skin care treatments, full body waxing and makeup application. Our spa colors are dark purples and greys and we are not opposed to additional colors that would complement those colors. We do a lot of eyelash extensions and while we do what those services listed we would like the skin care treatments to be in an area that would be noticed first. One of the attachments lists all of our services, descriptions and prices (please be sure to include all services and pricing. descriptions if possible). And our website has more information about us if needed. The website was not professionally done. So it DOESN'T represent our style exactly.

I HAVE ATTACHED A FEW PHOTOS BUT THEY DON'T HAVE TO BE USED.

Target Market(s)

women who would like to look their best, 35-55, annual income of 100,000+, she is usually busy and her children (if she has any) are high school age or older.

Industry/Entity Type

It Service

Font styles to use
Serif
Sans Serif

Requirements
Must have
• Must list all of our services. If it works to have the descriptions that would be great.
Nice to have
• If it works to have the descriptions of each service that would be great.

```html
<!DOCTYPE html>
<html lang="en">
<head>
<meta charset="utf-8">
<title>Velora Lash &amp; Skin Spa — Service Menu</title>
<link rel="stylesheet" href="https://fonts.googleapis.com/css2?family=Montserrat:wght@300;400;600;700&display=swap">
<style>
:root{
  --teal:#82cdc8;
  --teal-soft:#b5e2de;
  --plum-dark:#2e0f33;
  --plum:#5c3d66;
  --lilac:#a894b4;
  --mist:#f4f2f6;
  --white:#ffffff;
  --text:#2b1f2e;
}
*{margin:0;padding:0;box-sizing:border-box}
html,body{width:1200px;height:849px;overflow:hidden;background:var(--white)}
body{font-family:"Montserrat",sans-serif;color:var(--text)}
.sheet{position:relative;width:1200px;height:849px;overflow:hidden}

/* left panel */
.panel-services{position:absolute;left:0;top:0;width:400px;height:849px;background:var(--teal);overflow:hidden}
.hero-photo{position:absolute;left:17px;top:5px;width:430px;height:430px;border-radius:50%;
  background:radial-gradient(circle at 60% 30%,#fff6c8 0%,#f3d28a 35%,#d99a55 65%,#b56a4a 100%)}
.brand-small{position:absolute;left:210px;top:72px;color:var(--plum-dark);font-weight:600;line-height:1}
.brand-small .name{font-size:34px;display:block}
.brand-small .tag{font-size:10px;display:block;margin-top:2px;padding-left:52px}
.service-list{position:absolute;left:25px;top:451px;list-style:none}
.service-list li{display:flex;align-items:center;height:61.5px}
.service-list .icon{width:38px;height:38px;border-radius:50%;background:var(--plum);display:flex;align-items:center;justify-content:center;margin-right:35px}
.service-list .label{color:var(--white);font-weight:700;font-size:16.5px;letter-spacing:2.6px}
.footer-bar{position:absolute;left:0;bottom:0;width:400px;height:22px;background:var(--plum-dark)}

/* middle + right */
.panel-cover{position:absolute;left:400px;top:0;width:800px;height:849px;
  background:linear-gradient(180deg,var(--mist) 0%,#ede8f0 40%,#cbbcd3 62%,var(--lilac) 100%)}
.tulip-field{position:absolute;left:0;top:430px;width:800px;height:419px;
  background:linear-gradient(180deg,rgba(168,148,180,0) 0%,rgba(150,126,166,.55) 45%,rgba(120,96,138,.8) 100%)}

.contact{position:absolute;left:450px;top:62px;width:300px;text-align:center;font-size:13px;line-height:20px}
.contact h2{font-size:12.5px;font-weight:700;letter-spacing:.5px;color:var(--plum-dark)}
.contact .store{margin:14px auto 22px;width:58px;height:58px;border-radius:50%;background:var(--plum);display:flex;align-items:center;justify-content:center}
.contact p{margin-bottom:20px}
.hours h2{margin-bottom:20px}
.hours dt{font-weight:700;color:var(--plum-dark)}
.hours dd{margin-bottom:20px}

.brand-mid{position:absolute;left:450px;top:660px;width:300px;text-align:center;color:var(--plum-dark);font-weight:600;line-height:1}
.brand-mid .name{font-size:36px;display:block}
.brand-mid .tag{font-size:10px;display:block;margin-top:3px}
.website{position:absolute;left:450px;top:794px;width:300px;text-align:center;font-size:16px;font-weight:600;letter-spacing:2.4px;color:var(--plum-dark)}

.brand-main{position:absolute;left:852px;top:62px;color:var(--plum-dark);font-weight:600;line-height:1}
.brand-main .name{font-size:84px;display:block;letter-spacing:-1px}
.brand-main .tag{font-size:20px;display:block;margin-top:4px;padding-left:154px}

.photo{position:absolute;border-radius:50%}
.photo-facial{left:816px;top:184px;width:312px;height:312px;background:radial-gradient(circle at 40% 40%,#f4e2d6,#d9b39a 60%,#b98a72)}
.photo-makeup{left:1022px;top:366px;width:166px;height:166px;border:4px solid var(--plum-dark);background:radial-gradient(circle at 50% 45%,#f6e6dc,#e2bfa9 70%,#c89d86)}
.photo-device{left:970px;top:506px;width:156px;height:156px;border:5px solid var(--teal);background:radial-gradient(circle at 45% 55%,#eadcd8,#cfb4ae 65%,#a9c7cc)}
.arc{position:absolute;left:0;top:0}

.menu-bar{position:absolute;left:852px;top:730px;width:336px;height:38px;background:var(--plum-dark);color:var(--white);font-weight:300;font-size:22px;letter-spacing:5px;text-align:center;line-height:38px}
.swoosh{position:absolute;left:400px;top:735px}
</style>
</head>
<body>
<main class="sheet">

  <section class="panel-services">
    <div class="hero-photo" role="img" aria-label="Woman in a summer dress standing in a golden wheat field at sunset"></div>
    <div class="brand-small"><span class="name">Velora</span><span class="tag">Lash &amp; Skin Spa</span></div>
    <ul class="service-list">
      <li><span class="icon"><svg width="20" height="20" viewBox="0 0 20 20"><circle cx="10" cy="8" r="6" fill="#fff"/><rect x="8" y="12" width="5" height="7" fill="#fff"/></svg></span><span class="label">FACIAL &amp; SKIN TREATMENTS</span></li>
      <li><span class="icon"><svg width="22" height="22" viewBox="0 0 22 22"><circle cx="11" cy="11" r="5" fill="#fff"/><g stroke="#fff" stroke-width="1.6"><line x1="11" y1="1" x2="11" y2="4"/><line x1="11" y1="18" x2="11" y2="21"/><line x1="1" y1="11" x2="4" y2="11"/><line x1="18" y1="11" x2="21" y2="11"/><line x1="4" y1="4" x2="6" y2="6"/><line x1="16" y1="16" x2="18" y2="18"/><line x1="4" y1="18" x2="6" y2="16"/><line x1="16" y1="6" x2="18" y2="4"/></g></svg></span><span class="label">PEELS</span></li>
      <li><span class="icon"><svg width="10" height="26" viewBox="0 0 10 26"><rect x="4" y="0" width="2" height="12" fill="#fff"/><rect x="3" y="12" width="4" height="14" fill="#fff"/></svg></span><span class="label">EYELASHES</span></li>
      <li><span class="icon"><svg width="26" height="16" viewBox="0 0 26 16"><path d="M1 8 Q13 -2 25 8 Q13 18 1 8Z" fill="#fff"/><circle cx="13" cy="8" r="3" fill="#5c3d66"/></svg></span><span class="label">TINTING</span></li>
      <li><span class="icon"><svg width="16" height="24" viewBox="0 0 16 24"><circle cx="8" cy="4" r="3.5" fill="#fff"/><path d="M3 9 H13 L15 17 H11 V24 H5 V17 H1Z" fill="#fff"/></svg></span><span class="label">WAXING</span></li>
      <li><span class="icon"><svg width="22" height="20" viewBox="0 0 22 20"><ellipse cx="7" cy="7" rx="6" ry="5" fill="#fff"/><ellipse cx="15" cy="13" rx="6" ry="5" fill="#fff"/></svg></span><span class="label">MASSAGES</span></li>
    </ul>
    <div class="footer-bar"></div>
  </section>

  <section class="panel-cover">
    <div class="tulip-field" role="img" aria-label="Soft-focus field of pale purple tulips"></div>
  </section>

  <section class="contact">
    <h2>VISIT US</h2>
    <div class="store"><svg width="30" height="28" viewBox="0 0 30 28"><rect x="3" y="4" width="24" height="20" fill="#fff"/><rect x="6" y="0" width="18" height="5" fill="#fff"/><g fill="#5c3d66"><rect x="6" y="8" width="5" height="3"/><rect x="13" y="8" width="4" height="3"/><rect x="19" y="8" width="5" height="3"/><rect x="6" y="14" width="5" height="3"/><rect x="19" y="14" width="5" height="3"/><rect x="13" y="14" width="4" height="10"/></g><rect x="0" y="24" width="30" height="2" fill="#fff"/></svg></div>
    <p>2418 Briarwood Ln<br>Cedar Hollow, MO 63390</p>
    <p>hello@veloraspa.com<br>555-214-0387</p>
    <div class="hours">
      <h2>TRADING HOURS</h2>
      <dl>
        <dt>Tuesday</dt><dd>11:00am - 6:00pm</dd>
        <dt>Wednesday-Friday</dt><dd>11:00am-8:00pm</dd>
        <dt>Saturday</dt><dd>10:00am - 3:00pm</dd>
        <dt>Sunday-Monday</dt><dd>Closed</dd>
      </dl>
    </div>
  </section>

  <div class="brand-mid"><span class="name">Velora</span><span class="tag">Lash &amp; Skin Spa</span></div>

  <div class="brand-main"><span class="name">Velora</span><span class="tag">Lash &amp; Skin Spa</span></div>

  <svg class="arc" width="1200" height="849" aria-hidden="true"><path d="M972 186 A156 156 0 0 1 1128 342" fill="none" stroke="var(--plum-dark)" stroke-width="4" transform="translate(0 0)"/><path d="M972 186 A160 160 0 0 1 1128 350" fill="none" stroke="var(--plum-dark)" stroke-width="3"/></svg>
  <div class="photo photo-facial" role="img" aria-label="Client relaxing during a facial massage"></div>
  <div class="photo photo-makeup" role="img" aria-label="Makeup brush applying powder"></div>
  <div class="photo photo-device" role="img" aria-label="Skin treatment device in use"></div>

  <svg class="swoosh" width="800" height="114" aria-hidden="true">
    <path d="M0 68 Q140 -10 340 10 Q460 30 560 40 L790 50 L790 82 Q600 70 470 46 Q280 10 0 68Z" fill="var(--teal)"/>
    <path d="M452 40 L790 50 L790 62 L452 50Z" fill="var(--teal-soft)"/>
  </svg>
  <div class="menu-bar">SERVICE MENU</div>
  <div class="website">www.veloraspa.com</div>

</main>
</body>
</html>
```